Roll label Flyer design

I need a flyer for a roll label printer
Pictures for the project are located here:
https://plimtonstickers.sharefile.com/d-k4wq7812m3a0z551

Text I want is located here:
https://plimtonstickers.com/roll-labels.php

Target Market(s)

Manufactures, wholesalers

Industry/Entity Type

Printing

Requirements
Must have
• Lots of pictures. Our phone number 800-472-8164. Website www.plimtonstickers.com

```html
<!DOCTYPE html>
<html lang="en">
<head>
<meta charset="utf-8">
<title>Plimton Stickers — Roll Label Flyer</title>
<link rel="stylesheet" href="https://fonts.googleapis.com/css2?family=Bebas+Neue&family=Oswald:wght@400;500&display=swap">
<style>
  :root {
    --brand-red: #b7212b;
    --ink: #2b2b2b;
    --ghost: #ececec;
    --paper: #ffffff;
    --steel-dark: #3c4046;
    --steel: #8d939a;
    --steel-light: #d9dcdf;
    --machine-white: #eceef0;
    --pillar-yellow: #e2c63a;
    --warm-wood: #b48a62;
    --label-orange: #d9783f;
  }
  * { margin: 0; padding: 0; box-sizing: border-box; }
  html, body { width: 927px; height: 1200px; overflow: hidden; background: var(--paper); }
  .flyer { position: relative; width: 927px; height: 1200px; overflow: hidden; background: var(--paper); font-family: "Oswald", sans-serif; }

  .hero-photo {
    position: absolute; left: 0; top: 0; width: 927px; height: 632px;
    background:
      radial-gradient(ellipse 60px 330px at 790px 260px, rgba(226,198,58,0.85), rgba(226,198,58,0) 100%),
      radial-gradient(ellipse 320px 230px at 650px 420px, rgba(236,238,240,0.95), rgba(236,238,240,0) 100%),
      radial-gradient(ellipse 140px 90px at 870px 280px, rgba(183,33,43,0.45), rgba(183,33,43,0) 100%),
      radial-gradient(ellipse 110px 60px at 580px 365px, rgba(183,33,43,0.35), rgba(183,33,43,0) 100%),
      radial-gradient(ellipse 120px 150px at 270px 330px, rgba(40,42,48,0.75), rgba(40,42,48,0) 100%),
      radial-gradient(ellipse 230px 170px at 180px 560px, rgba(220,214,204,0.9), rgba(220,214,204,0) 100%),
      radial-gradient(ellipse 180px 140px at 380px 230px, rgba(180,138,98,0.45), rgba(180,138,98,0) 100%),
      radial-gradient(ellipse 90px 120px at 900px 140px, rgba(60,64,70,0.7), rgba(60,64,70,0) 100%),
      linear-gradient(180deg, #a9aeb4 0%, #c6c9cc 22%, #9da2a8 48%, #b8bbbe 70%, #7f858c 100%);
  }
  .brand-tab {
    position: absolute; left: 23px; top: 0; width: 313px; height: 110px;
    background: var(--brand-red); display: flex; align-items: center; gap: 14px; padding-left: 22px;
  }
  .brand-tab .mark { flex: none; width: 44px; height: 44px; border-radius: 50%; background: var(--paper); }
  .brand-tab .name { color: var(--paper); font-family: "Oswald", sans-serif; font-weight: 400; font-size: 22px; letter-spacing: 2.5px; text-transform: uppercase; white-space: nowrap; }

  .ghost-word {
    position: absolute; font-family: "Bebas Neue", sans-serif; color: var(--ghost);
    line-height: 1; user-select: none; white-space: nowrap;
  }
  .ghost-word.upper { left: 436px; top: 640px; font-size: 196px; letter-spacing: 28px; }
  .ghost-word.lower { left: 40px; top: 935px; font-size: 180px; letter-spacing: 22px; }

  .headline { position: absolute; left: 24px; top: 660px; }
  .headline .kicker {
    position: absolute; left: 0; top: 0; height: 160px; width: 36px;
    writing-mode: vertical-rl; transform: rotate(180deg);
    font-family: "Bebas Neue", sans-serif; font-size: 38px; color: var(--ink); line-height: 36px; letter-spacing: 1px; text-align: center; white-space: nowrap;
  }
  .headline .kicker .accent { color: var(--brand-red); }
  .headline .line {
    position: absolute; left: 44px; font-family: "Bebas Neue", sans-serif; font-size: 100px; line-height: 1; letter-spacing: 4px;
    background: linear-gradient(180deg, #6b6f74 0%, #2e3034 100%); -webkit-background-clip: text; background-clip: text; color: transparent; white-space: nowrap;
  }
  .headline .line.first { top: -6px; }
  .headline .line.second { top: 76px; }

  .photo-strip { position: absolute; top: 849px; left: 23px; display: flex; gap: 6px; }
  .photo-strip .thumb { width: 173px; height: 116px; }
  .thumb.t1 {
    background:
      radial-gradient(ellipse 70px 40px at 70px 35px, rgba(217,120,63,0.9), rgba(217,120,63,0) 100%),
      radial-gradient(ellipse 80px 40px at 80px 85px, rgba(217,120,63,0.8), rgba(217,120,63,0) 100%),
      radial-gradient(ellipse 50px 60px at 150px 40px, rgba(60,64,70,0.6), rgba(60,64,70,0) 100%),
      linear-gradient(180deg, #f1e7da, #e6d6c2);
  }
  .thumb.t2 {
    background:
      radial-gradient(ellipse 70px 45px at 105px 45px, rgba(30,32,36,0.95), rgba(30,32,36,0) 100%),
      radial-gradient(ellipse 60px 35px at 95px 92px, rgba(40,42,46,0.8), rgba(40,42,46,0) 100%),
      radial-gradient(ellipse 40px 40px at 30px 50px, rgba(226,198,58,0.55), rgba(226,198,58,0) 100%),
      linear-gradient(135deg, #c9ccd0, #7d8288);
  }
  .thumb.t3 {
    background:
      radial-gradient(ellipse 85px 30px at 86px 58px, rgba(236,238,240,0.85), rgba(236,238,240,0) 100%),
      radial-gradient(ellipse 60px 40px at 30px 30px, rgba(180,138,98,0.5), rgba(180,138,98,0) 100%),
      linear-gradient(180deg, #2e3034, #4a4e54 55%, #2a2c30);
  }
  .thumb.t4 {
    background:
      radial-gradient(ellipse 80px 35px at 90px 55px, rgba(236,238,240,0.9), rgba(236,238,240,0) 100%),
      radial-gradient(ellipse 60px 50px at 30px 95px, rgba(50,54,60,0.7), rgba(50,54,60,0) 100%),
      linear-gradient(135deg, #a7acb2, #5f646b);
  }
  .thumb.t5 {
    background:
      radial-gradient(ellipse 60px 22px at 105px 48px, rgba(240,240,240,0.95), rgba(240,240,240,0) 100%),
      radial-gradient(ellipse 55px 30px at 110px 95px, rgba(183,33,43,0.55), rgba(183,33,43,0) 100%),
      radial-gradient(ellipse 50px 60px at 25px 60px, rgba(40,42,46,0.7), rgba(40,42,46,0) 100%),
      linear-gradient(135deg, #b5b9be, #6c7178);
  }

  .services {
    position: absolute; left: 0; width: 927px; top: 988px; text-align: center;
    font-family: "Oswald", sans-serif; font-weight: 500; font-size: 21px; color: var(--brand-red); letter-spacing: 0.3px; white-space: nowrap;
  }

  .footer-band { position: absolute; left: 0; top: 1056px; width: 927px; height: 144px; background: var(--brand-red); color: var(--paper); }
  .footer-band .contact { position: absolute; right: 14px; top: 20px; text-align: right; font-style: normal; font-size: 18px; line-height: 27px; font-weight: 400; letter-spacing: 0.4px; white-space: nowrap; }
  .footer-band .site { position: absolute; left: 12px; bottom: 12px; font-size: 18px; letter-spacing: 0.4px; }
</style>
</head>
<body>
<main class="flyer">
  <div class="hero-photo" role="img" aria-label="Press operator working at a roll label printing press in a production plant, yellow crane pillar and white press units behind"></div>

  <header class="brand-tab">
    <span class="mark"></span>
    <span class="name">Plimton Stickers</span>
  </header>

  <div class="ghost-word upper" aria-hidden="true">LABEL</div>
  <div class="ghost-word lower" aria-hidden="true">LABEL</div>

  <h1 class="headline">
    <span class="kicker">We<span class="accent">’</span>re your</span>
    <span class="line first">Perfect</span>
    <span class="line second">Print Partner</span>
  </h1>

  <section class="photo-strip">
    <div class="thumb t1" role="img" aria-label="Rolls of printed orange price labels"></div>
    <div class="thumb t2" role="img" aria-label="Roll of black product labels on a press spindle"></div>
    <div class="thumb t3" role="img" aria-label="Strip of printed warning labels running through the press"></div>
    <div class="thumb t4" role="img" aria-label="Close-up of label web passing over press rollers"></div>
    <div class="thumb t5" role="img" aria-label="Printed label roll feeding through a finishing station"></div>
  </section>

  <p class="services">Providing Decals, Labels, Banners, Counter Mats, Domed Decals,and Security Products</p>

  <footer class="footer-band">
    <address class="contact">
      1180 North Alder Street, Suite #210 Tacoma, WA 98403<br>
      Toll Free: (800) 472-8164<br>
      Fax: (253) 318-4076<br>
      Hours: Monday-Friday 8-5 Pacific Time
    </address>
    <div class="site">plimtonstickers.com</div>
  </footer>
</main>
</body>
</html>
```